Smart Home App Needs 4 Mockup Screens. Extra Work Guaranteed for Winner

BACKGROUND
Our company, Lumora, is launching an exciting new app early next year. And we need some examples of what our app will look like to show to some of the biggest retailers in the world. We hope that this project will lead to regular work as we have a lot of new products planned for the app.

Our app will support baby, home and pet monitors (cameras) as well as the world's first smart pet flap.

The monitors allow you to do much more than just watch live video. By monitoring and providing information on sound, movement and temperature the app provides the user with instant peace of mind wherever they are. If anything has changed the user can be alerted via notifications. If motion is detected the user will receive a clip of the whole event moments after it has happened.

The Smart Pet Flap is packed full of features too. From letting you decide when your pet can or can't go outside from your mobile, to automatically opening if a fire is detected (along with a whole host of other features) - this really is the most advanced pet flap in the world.

REQUIREMENTS
We need 4 mock-up screens creating to show the UI of our app.
1. Camera Home Page
2. Camera Notifications Page
3. Pet Flap Fire Alarm Warning Page
4. Extreme Weather Warning Page

Optional - Happy to Pay the Winner Extra for these Designs
5. Start Up/Log In Page
6. Pet Flap Notification Example
7. Pet Flap Scheduler Page (your choice)
(SEE LUMORA APP DESIGN COMPETITION - ATTACHED)

STYLE GUIDE
As you'll see from our wireframes we want our app to be very minimal and modern. The predominant colour will be white but where colour is used it should be bright (see our colour palette - which we will provide shortly).

INSPIRATION
We love the UI of Finchly (home surveillance). Also check out Vesk (smart thermostat).
(SEE LUMORA UI EXAMPLES ATTACHED)

LOGO
We love our logo. Feel free to use it in creative ways.

So far we're also using it as a kind of beacon to indicate if everything is ok.

LOGO COLOURS & APP COLOURS
As mentioned, we are thinking of using the green logo to indicate that everything is ok (and also for the pet app in general). We reserve red for when something has happened (normally bad) and needs attention, like a fire alarm going off.

The app will be predominantly black and white with the odd minimal flash of colour (probably primary colour)
We'll upload a colour scheme as soon as we have it.

CONTACT
Please message us for more details - we'll do our best to reply promptly.

FUTURE WORK
We will need extra screens made straight after the competition is over and there should be additional regular work after this.

Target Market(s)

Our app will be used by young professionals, to young parents to grandparents. The design must be contemporary but timeless and easy to use no matter how good you are with technology.

Industry/Entity Type

Pet

Font styles to use
Sans Serif

Colors
faee3f
33a6d7
ec1f27
acd036
32b7a4

Requirements
Must have
• Beautiful, minimal design. Make sure you spend time looking at the Finchly and Vesk apps before starting.

For the videos make sure you use sensible images - that you'd expect to see from a monitor (high resolution images if possible)
Nice to have
• Creative use of our logo.
Should not have
• Too much detail/clutter/colours. Ugly fonts.

```html
<!DOCTYPE html>
<html lang="en">
<head>
<meta charset="utf-8">
<title>Lumora – Lock Screen Notification</title>
<link rel="stylesheet" href="https://fonts.googleapis.com/css2?family=Roboto:wght@100;300;400;700&display=swap">
<style>
  :root {
    --page-bg: #e6e6e6;
    --status-bg: #f2f2f2;
    --status-ink: #111111;
    --sky-top: #1f5fc4;
    --sky-mid: #4a8fe0;
    --city-tone: #9fb4c4;
    --trees: #3d7a3a;
    --shore: #c9b08a;
    --water-top: #2a87c9;
    --water-bottom: #1f5e96;
    --clock-ink: #ffffff;
    --date-ink: rgba(255, 255, 255, 0.8);
    --panel-bg: rgba(40, 44, 48, 0.88);
    --panel-ink: #ffffff;
    --brand-dot: #acd036;
  }
  * { margin: 0; padding: 0; box-sizing: border-box; }
  html, body {
    width: 908px;
    height: 1200px;
    overflow: hidden;
    background: var(--page-bg);
    font-family: "Roboto", "Helvetica Neue", Arial, sans-serif;
  }
  .lock-screen {
    position: absolute;
    left: 116px;
    top: 0;
    width: 676px;
    height: 1200px;
    overflow: hidden;
  }
  .wallpaper {
    position: absolute;
    inset: 53px 0 0 0;
    background: linear-gradient(
      to bottom,
      var(--sky-top) 0%,
      var(--sky-mid) 38%,
      var(--city-tone) 52%,
      var(--trees) 64%,
      var(--shore) 70%,
      var(--water-top) 76%,
      var(--water-bottom) 100%
    );
  }
  .status-bar {
    position: absolute;
    top: 0; left: 0;
    width: 100%;
    height: 53px;
    background: var(--status-bg);
    color: var(--status-ink);
    font-size: 22px;
    font-weight: 400;
    display: flex;
    align-items: center;
    padding: 0 18px;
  }
  .status-bar .carrier { display: flex; align-items: center; gap: 8px; flex: 1; }
  .status-bar .status-time { flex: 1; text-align: center; font-weight: 700; white-space: nowrap; }
  .status-bar .battery { flex: 1; display: flex; justify-content: flex-end; align-items: center; gap: 8px; }
  .signal { display: flex; gap: 3px; }
  .signal span { width: 10px; height: 10px; border-radius: 50%; border: 1.5px solid var(--status-ink); }
  .signal span.on { background: var(--status-ink); }
  .clock {
    position: absolute;
    top: 92px;
    width: 100%;
    text-align: center;
    color: var(--clock-ink);
    font-weight: 100;
    font-size: 112px;
    line-height: 1;
    letter-spacing: 2px;
  }
  .date {
    position: absolute;
    top: 234px;
    width: 100%;
    text-align: center;
    color: var(--date-ink);
    font-weight: 300;
    font-size: 28px;
  }
  .notification {
    position: absolute;
    left: 98px;
    top: 462px;
    width: 471px;
    height: 268px;
    background: var(--panel-bg);
    color: var(--panel-ink);
    text-align: center;
  }
  .notification .brand {
    position: absolute;
    top: 70px;
    width: 100%;
    display: flex;
    justify-content: center;
    align-items: center;
    gap: 14px;
    font-weight: 700;
    font-size: 30px;
    letter-spacing: 1px;
  }
  .brand-dot { width: 34px; height: 34px; border-radius: 50%; background: var(--brand-dot); }
  .notification .message {
    position: absolute;
    top: 182px;
    width: 100%;
    font-size: 24px;
    font-weight: 400;
  }
</style>
</head>
<body>
  <main class="lock-screen">
    <div class="wallpaper" role="img" aria-label="Photo of a harbour city skyline under a blue sky with trees, a waterfront building and blue water"></div>

    <header class="status-bar">
      <div class="carrier">
        <div class="signal"><span class="on"></span><span class="on"></span><span class="on"></span><span></span><span></span></div>
        <span>KELVO</span>
        <svg width="24" height="18" viewBox="0 0 24 18" aria-hidden="true">
          <path d="M2 6 A14 14 0 0 1 22 6" fill="none" stroke="currentColor" stroke-width="2.4"/>
          <path d="M6 10 A8.5 8.5 0 0 1 18 10" fill="none" stroke="currentColor" stroke-width="2.4"/>
          <circle cx="12" cy="15" r="2.4" fill="currentColor"/>
        </svg>
      </div>
      <div class="status-time">4:21 PM</div>
      <div class="battery">
        <span>100%</span>
        <svg width="44" height="20" viewBox="0 0 44 20" aria-hidden="true">
          <rect x="1" y="2" width="38" height="16" rx="2" fill="none" stroke="currentColor" stroke-width="2"/>
          <rect x="4" y="5" width="32" height="10" fill="currentColor"/>
          <rect x="40" y="7" width="3" height="6" fill="currentColor"/>
        </svg>
      </div>
    </header>

    <div class="clock">04:42</div>
    <div class="date">Wednesday 23 October</div>

    <section class="notification">
      <div class="brand"><span class="brand-dot"></span><span>LUMORA</span></div>
      <p class="message">Mango has just got home!</p>
    </section>
  </main>
</body>
</html>
```